Dental Medical History Form - Content provided

Design a medical history form for a dental practice. Content is provided so all that is needed is the formatting to make it look great and easy to read.

"Patient Information" to include all information contained in top portion of the "Patient Medical History Form" docx file.

"Medical History" should follow the formatting and content of the "Exact Medical History" file as this is what the entry fields look like in our practice software and so we would like it to match.

1st page - Patient info, allergies, medications, antibiotics, joint replacement, pregnancy.

2nd page - Do you have, or have you had, any of the following? . . . . . . .
Updates

Project Deadline Extended Reason: Picked too short of a deadline to start (2 days) Added Monday, February 13, 2017

Target Market(s)

All ages but must be clear enough for elderly to read. Use as much space as possible to keep font size bigger yet keep to two pages

Industry/Entity Type

Dental

Font styles to use
Sans Serif

Requirements
Must have
• All content provided
• Our logo at the top (file provided)
• Century Gothic Font
• Limit to two pages

```html
<!DOCTYPE html>
<html lang="en">
<head>
<meta charset="utf-8">
<title>Harbour Dental – Confidential Medical History</title>
<link href="https://fonts.googleapis.com/css2?family=Mulish:ital,wght@0,300;0,400;0,700;1,400&display=swap" rel="stylesheet">
<style>
:root{
  --bg:#c9c9cd;
  --paper:#ffffff;
  --ink:#2b2f33;
  --brand:#3b4a55;
  --rule:#b9bcc0;
  --muted:#5a6670;
}
*{box-sizing:border-box;margin:0;padding:0}
html,body{width:1200px;height:1037px;overflow:hidden}
body{background:var(--bg);font-family:"Mulish",sans-serif;color:var(--ink);position:relative}
.page{position:absolute;top:138px;width:551px;height:778px;background:var(--paper)}
.page--info{left:38px}
.page--history{left:610px}
.t{position:absolute;white-space:nowrap;font-size:8px;font-weight:700;line-height:10px}
.brand{position:absolute;left:34px;top:44px;font-size:27px;font-weight:300;color:var(--brand);letter-spacing:.5px}
.contact{position:absolute;left:360px;top:34px;font-size:7.5px;font-weight:700;color:var(--ink)}
.contact li{list-style:none;display:flex;align-items:flex-start;gap:9px;margin-bottom:7px;line-height:9px}
.contact svg{width:11px;height:11px;flex:none}
.header-rule{position:absolute;left:0;top:94px;width:551px;height:6px}
.title{position:absolute;top:117px;width:100%;text-align:center;font-size:12px;font-weight:700;text-decoration:underline;text-underline-offset:2px}
.box{position:absolute;left:30px;width:490px;border:1.5px solid var(--rule)}
.field{position:absolute;display:flex;align-items:flex-end;font-size:8px;font-weight:700;line-height:10px;height:10px}
.field .line{flex:1;border-bottom:1px solid var(--ink);margin-left:1px;height:9px}
.o{display:inline-block;width:10px;height:10px;border:1px solid var(--ink);border-radius:50%;vertical-align:-2px;margin-left:1px}
.tick{display:inline-block;width:14px;height:14px;vertical-align:-4px;margin:0 4px}
.blank{position:absolute;height:0;border-bottom:1px solid var(--ink)}
.footer{position:absolute;left:0;top:715px;width:551px;height:63px;background:var(--brand);color:#fff}
.turnover{position:absolute;left:451px;top:13px;font-size:8px;font-style:italic;font-weight:700}
.thanks{text-align:center;padding-top:11px;font-size:7px;font-style:italic;line-height:9.5px}
.history{position:absolute;left:25px;top:112px;width:495px;height:594px;border:1.5px solid var(--rule)}
.history-q{position:absolute;left:7px;top:6px;font-size:8px;font-weight:700}
.col{position:absolute;top:28px;width:240px;font-size:8px;line-height:12px}
.col--a{left:7px}
.col--b{left:252px}
.row{display:flex;height:12px}
.row .name{width:171px;white-space:nowrap}
.row .yn{white-space:nowrap}
.row .yn .o{width:10px;height:10px;margin-right:4px}
.group{font-weight:700;text-decoration:underline;height:12px}
.gap{height:12px}
.sign{position:absolute;display:flex;align-items:flex-end;font-size:8px;font-weight:700;height:10px}
.sign .line{flex:1;border-bottom:1px solid var(--ink);height:9px;margin-left:1px}
</style>
</head>
<body>

<svg width="0" height="0" style="position:absolute">
  <defs>
    <symbol id="i-pin" viewBox="0 0 12 12"><path d="M6 0.5a4 4 0 0 0-4 4c0 3 4 7 4 7s4-4 4-7a4 4 0 0 0-4-4z" fill="none" stroke="#2b2f33" stroke-width="1.4"/><circle cx="6" cy="4.5" r="1.4" fill="#2b2f33"/></symbol>
    <symbol id="i-phone" viewBox="0 0 12 12"><path d="M1 4c0-1.5 2-2.5 5-2.5s5 1 5 2.5v1H8.5V3.8H3.5V5H1z" fill="#2b2f33"/><rect x="2.5" y="6" width="7" height="4.5" rx="1" fill="#2b2f33"/><circle cx="6" cy="8.2" r="1.2" fill="#fff"/></symbol>
    <symbol id="i-arrow" viewBox="0 0 12 12"><path d="M7.5 0.5L3 11.5l2.2-1 1-4.2 3.3-3z" fill="#2b2f33"/></symbol>
    <symbol id="i-tick" viewBox="0 0 14 14"><circle cx="7" cy="7" r="7" fill="#3b4a55"/><path d="M3.8 7.2l2.2 2.2 4.2-4.6" fill="none" stroke="#fff" stroke-width="1.6"/></symbol>
    <symbol id="i-rule" viewBox="0 0 551 6"><rect x="0" y="4" width="551" height="1.2" fill="#3b4a55"/><path d="M0 0h188l6 5H0z" fill="#3b4a55"/></symbol>
  </defs>
</svg>

<!-- Page 1: patient information -->
<section class="page page--info">
  <div class="brand">Harbour Dental</div>
  <ul class="contact">
    <li><svg><use href="#i-pin"/></svg><span>Suite 4/18 Bayview Rd<br>Kincumber NSW 2251</span></li>
    <li><svg><use href="#i-phone"/></svg><span>(02) 5550 1234</span></li>
    <li><svg><use href="#i-arrow"/></svg><span>www.harbourdental.example</span></li>
  </ul>
  <svg class="header-rule"><use href="#i-rule"/></svg>

  <h1 class="title">CONFIDENTIAL MEDICAL HISTORY</h1>

  <div class="box" style="top:143px;height:187px"></div>
  <div class="field" style="left:40px;top:151px;width:216px">Name:<span class="line"></span></div>
  <div class="t" style="left:40px;top:164px">Title</div>
  <div class="t" style="left:96px;top:164px">First</div>
  <div class="t" style="left:144px;top:164px">Middle</div>
  <div class="t" style="left:208px;top:164px">Last</div>
  <div class="field" style="left:40px;top:189px;width:216px">Address:<span class="line"></span></div>
  <div class="field" style="left:40px;top:202px;width:216px">DOB:<span class="line"></span></div>
  <div class="field" style="left:40px;top:215px;width:216px">Email Address:<span class="line"></span></div>
  <div class="field" style="left:40px;top:228px;width:216px">Phone Number(s):<span class="line"></span></div>
  <div class="t" style="left:124px;top:241px">Mobile</div>
  <div class="t" style="left:166px;top:241px">Work</div>
  <div class="t" style="left:200px;top:241px">Home</div>
  <div class="t" style="left:40px;top:267px">Emergency Contact Person:</div>
  <div class="field" style="left:40px;top:280px;width:216px">Name:<span class="line"></span></div>
  <div class="field" style="left:40px;top:293px;width:216px">Relationship:<span class="line"></span></div>
  <div class="field" style="left:40px;top:305px;width:216px">Phone number:<span class="line"></span></div>

  <div class="t" style="left:272px;top:151px">General Practitioner:</div>
  <div class="field" style="left:272px;top:164px;width:240px">Name:<span class="line"></span></div>
  <div class="field" style="left:272px;top:177px;width:240px">Practice Name:<span class="line"></span></div>
  <div class="field" style="left:272px;top:189px;width:240px">Phone Number:<span class="line"></span></div>
  <div class="t" style="left:272px;top:215px">Do you have a health fund with dental cover?&nbsp; Yes&nbsp; or No</div>
  <div class="field" style="left:272px;top:228px;width:240px">If so, what is the name of the fund?<span class="line"></span></div>
  <div class="field" style="left:272px;top:241px;width:240px">Fund Number?<span class="line"></span></div>
  <div class="t" style="left:272px;top:254px">Priority Number on card: 0&nbsp; 1&nbsp; 2&nbsp; 3&nbsp; 4&nbsp; 5</div>
  <div class="field" style="left:272px;top:280px;width:240px">Occupation:<span class="line"></span></div>
  <div class="field" style="left:272px;top:293px;width:240px">Referred by:<span class="line"></span></div>

  <div class="box" style="top:343px;height:74px"></div>
  <div class="t" style="left:40px;top:350px">Please indicate if&nbsp; you are allergic to any of the following<svg class="tick"><use href="#i-tick"/></svg>?</div>
  <div class="t" style="left:40px;top:373px">Aspirin<span class="o"></span></div>
  <div class="t" style="left:90px;top:373px">Codeine<span class="o"></span></div>
  <div class="t" style="left:152px;top:373px">Penicillin<span class="o"></span></div>
  <div class="t" style="left:216px;top:373px">Sulfites<span class="o"></span></div>
  <div class="t" style="left:269px;top:373px">Latex<span class="o"></span></div>
  <div class="t" style="left:314px;top:373px">Local Anaesthetic<span class="o"></span></div>
  <div class="t" style="left:407px;top:373px">Lactose<span class="o"></span></div>
  <div class="t" style="left:464px;top:373px">Nickel<span class="o"></span></div>
  <div class="field" style="left:40px;top:395px;width:472px">Other:<span class="line"></span></div>

  <div class="box" style="top:430px;height:74px"></div>
  <div class="t" style="left:40px;top:438px">Are you currently taking, or have ever taken, any of the following medication<svg class="tick"><use href="#i-tick"/></svg>?</div>
  <div class="t" style="left:40px;top:459px">Asthma inhaler<span class="o"></span></div>
  <div class="t" style="left:120px;top:459px">Anti-epileptics<span class="o"></span></div>
  <div class="t" style="left:200px;top:459px">Anti-depressants<span class="o"></span></div>
  <div class="t" style="left:288px;top:459px">Blood Pressure<span class="o"></span></div>
  <div class="t" style="left:368px;top:459px">Blood Thinners<span class="o"></span></div>
  <div class="t" style="left:40px;top:482px">Bisphosphonates<span class="o"></span></div>
  <div class="t" style="left:128px;top:482px">Chemotherapy<span class="o"></span></div>
  <div class="t" style="left:208px;top:482px">Insulin<span class="o"></span></div>
  <div class="t" style="left:256px;top:482px">Immunosuppressants<span class="o"></span></div>
  <div class="t" style="left:360px;top:482px">Steroids<span class="o"></span></div>
  <div class="t" style="left:408px;top:482px">Oral Contraceptive<span class="o"></span></div>

  <div class="box" style="top:518px;height:70px"></div>
  <div class="t" style="left:40px;top:525px">Please specify medication name, dose, and frequency where possible:</div>
  <div class="blank" style="left:40px;top:547px;width:144px"></div>
  <div class="blank" style="left:40px;top:560px;width:144px"></div>
  <div class="blank" style="left:40px;top:573px;width:144px"></div>
  <div class="blank" style="left:200px;top:547px;width:144px"></div>
  <div class="blank" style="left:200px;top:560px;width:144px"></div>
  <div class="blank" style="left:200px;top:573px;width:144px"></div>
  <div class="blank" style="left:360px;top:547px;width:144px"></div>
  <div class="blank" style="left:360px;top:560px;width:144px"></div>
  <div class="blank" style="left:360px;top:573px;width:144px"></div>

  <div class="box" style="top:602px;height:96px"></div>
  <div class="t" style="left:40px;top:609px">Do you require antibiotic cover? Yes<span class="o"></span></div>
  <div class="t" style="left:216px;top:609px">No<span class="o"></span></div>
  <div class="t" style="left:40px;top:635px">Have you had a joint replacement? Yes<span class="o"></span></div>
  <div class="t" style="left:224px;top:635px">No<span class="o"></span></div>
  <div class="t" style="left:40px;top:660px">Women:</div>
  <div class="t" style="left:40px;top:674px">Are you pregnant? Yes<span class="o"></span></div>
  <div class="t" style="left:160px;top:674px">No<span class="o"></span></div>
  <div class="t" style="left:200px;top:674px">Possible or Breast Feeding? Yes<span class="o"></span></div>
  <div class="t" style="left:352px;top:674px">No<span class="o"></span></div>

  <footer class="footer"><span class="turnover">Please Turnover</span></footer>
</section>

<!-- Page 2: medical history -->
<section class="page page--history">
  <div class="brand">Harbour Dental</div>
  <ul class="contact">
    <li><svg><use href="#i-pin"/></svg><span>Suite 4/18 Bayview Rd<br>Kincumber NSW 2251</span></li>
    <li><svg><use href="#i-phone"/></svg><span>(02) 5550 1234</span></li>
    <li><svg><use href="#i-arrow"/></svg><span>www.harbourdental.example</span></li>
  </ul>
  <svg class="header-rule"><use href="#i-rule"/></svg>

  <div class="history">
    <p class="history-q">Do you have, or have you had, any of the following?</p>

    <div class="col col--a">
      <div class="group">Dental</div>
      <div class="row"><span class="name">Acid Reflux</span><span class="yn">Yes<span class="o"></span>No<span class="o"></span></span></div>
      <div class="row"><span class="name">Bad Breath/Taste</span><span class="yn">Yes<span class="o"></span>No<span class="o"></span></span></div>
      <div class="row"><span class="name">Bleeding/Swollen/Sore Gums</span><span class="yn">Yes<span class="o"></span>No<span class="o"></span></span></div>
      <div class="row"><span class="name">Blisters/Ulcers in Mouth</span><span class="yn">Yes<span class="o"></span>No<span class="o"></span></span></div>
      <div class="row"><span class="name">Broken tooth/filling</span><span class="yn">Yes<span class="o"></span>No<span class="o"></span></span></div>
      <div class="row"><span class="name">Burning tongue</span><span class="yn">Yes<span class="o"></span>No<span class="o"></span></span></div>
      <div class="row"><span class="name">Dry mouth</span><span class="yn">Yes<span class="o"></span>No<span class="o"></span></span></div>
      <div class="row"><span class="name">Food collection between teeth</span><span class="yn">Yes<span class="o"></span>No<span class="o"></span></span></div>
      <div class="row"><span class="name">Grinding/clenching teeth (day/night)</span><span class="yn">Yes<span class="o"></span>No<span class="o"></span></span></div>
      <div class="row"><span class="name">Loose teeth</span><span class="yn">Yes<span class="o"></span>No<span class="o"></span></span></div>
      <div class="row"><span class="name">Crooked teeth</span><span class="yn">Yes<span class="o"></span>No<span class="o"></span></span></div>
      <div class="row"><span class="name">Discoloured teeth</span><span class="yn">Yes<span class="o"></span>No<span class="o"></span></span></div>
      <div class="row"><span class="name">Sensitivity to Hot/Cold</span><span class="yn">Yes<span class="o"></span>No<span class="o"></span></span></div>
      <div class="row"><span class="name">Tooth pain when chewing</span><span class="yn">Yes<span class="o"></span>No<span class="o"></span></span></div>
      <div class="row"><span class="name">Jaw pain/Fracture</span><span class="yn">Yes<span class="o"></span>No<span class="o"></span></span></div>
      <div class="row"><span class="name">Orthodontic treatment/history</span><span class="yn">Yes<span class="o"></span>No<span class="o"></span></span></div>
      <div class="row"><span class="name">Oral Cancer</span><span class="yn">Yes<span class="o"></span>No<span class="o"></span></span></div>
      <div class="gap"></div>
      <div class="group">Diet/Lifestyle</div>
      <div class="row"><span class="name">Drink more than one glass alcohol per day</span><span class="yn">Yes<span class="o"></span>No<span class="o"></span></span></div>
      <div class="row"><span class="name">Smoking</span><span class="yn">Yes<span class="o"></span>No<span class="o"></span></span></div>
      <div class="row"><span class="name">Carbonated drinks</span><span class="yn">Yes<span class="o"></span>No<span class="o"></span></span></div>
      <div class="row"><span class="name">Sugary foods</span><span class="yn">Yes<span class="o"></span>No<span class="o"></span></span></div>
      <div class="gap"></div>
      <div class="group">Blood</div>
      <div class="row"><span class="name">Anaemia</span><span class="yn">Yes<span class="o"></span>No<span class="o"></span></span></div>
      <div class="row"><span class="name">Blood clots</span><span class="yn">Yes<span class="o"></span>No<span class="o"></span></span></div>
      <div class="row"><span class="name">Leukemia</span><span class="yn">Yes<span class="o"></span>No<span class="o"></span></span></div>
      <div class="row"><span class="name">Low platelets</span><span class="yn">Yes<span class="o"></span>No<span class="o"></span></span></div>
      <div class="row"><span class="name">Lymphoma</span><span class="yn">Yes<span class="o"></span>No<span class="o"></span></span></div>
      <div class="row"><span class="name">Haemophelia</span><span class="yn">Yes<span class="o"></span>No<span class="o"></span></span></div>
      <div class="gap"></div>
      <div class="group">Chest</div>
      <div class="row"><span class="name">Bronchitis</span><span class="yn">Yes<span class="o"></span>No<span class="o"></span></span></div>
      <div class="row"><span class="name">Cystic Fibrosis</span><span class="yn">Yes<span class="o"></span>No<span class="o"></span></span></div>
      <div class="row"><span class="name">Emphysema</span><span class="yn">Yes<span class="o"></span>No<span class="o"></span></span></div>
      <div class="row"><span class="name">Pneumonia</span><span class="yn">Yes<span class="o"></span>No<span class="o"></span></span></div>
      <div class="gap"></div>
      <div class="group">Infectious Disease</div>
      <div class="row"><span class="name">Creutzfeldt-Jakob Disease</span><span class="yn">Yes<span class="o"></span>No<span class="o"></span></span></div>
      <div class="row"><span class="name">Hepatitis A,B,C,D</span><span class="yn">Yes<span class="o"></span>No<span class="o"></span></span></div>
    </div>

    <div class="col col--b">
      <div class="gap"></div>
      <div class="row"><span class="name">HIV/AIDS</span><span class="yn">Yes<span class="o"></span>No<span class="o"></span></span></div>
      <div class="row"><span class="name">Influenza</span><span class="yn">Yes<span class="o"></span>No<span class="o"></span></span></div>
      <div class="row"><span class="name">Shingles</span><span class="yn">Yes<span class="o"></span>No<span class="o"></span></span></div>
      <div class="row"><span class="name">Tuberculosis</span><span class="yn">Yes<span class="o"></span>No<span class="o"></span></span></div>
      <div class="gap"></div>
      <div class="group">Heart</div>
      <div class="row"><span class="name">Angina</span><span class="yn">Yes<span class="o"></span>No<span class="o"></span></span></div>
      <div class="row"><span class="name">Atrial Fibrillation</span><span class="yn">Yes<span class="o"></span>No<span class="o"></span></span></div>
      <div class="row"><span class="name">Blood Pressure (High/Low)</span><span class="yn">Yes<span class="o"></span>No<span class="o"></span></span></div>
      <div class="row"><span class="name">Congenital Heart Disease</span><span class="yn">Yes<span class="o"></span>No<span class="o"></span></span></div>
      <div class="row"><span class="name">Heart attack</span><span class="yn">Yes<span class="o"></span>No<span class="o"></span></span></div>
      <div class="row"><span class="name">Heart murmur</span><span class="yn">Yes<span class="o"></span>No<span class="o"></span></span></div>
      <div class="row"><span class="name">Heart surgery</span><span class="yn">Yes<span class="o"></span>No<span class="o"></span></span></div>
      <div class="row"><span class="name">Heart valve replacement</span><span class="yn">Yes<span class="o"></span>No<span class="o"></span></span></div>
      <div class="row"><span class="name">Infective endocarditis</span><span class="yn">Yes<span class="o"></span>No<span class="o"></span></span></div>
      <div class="row"><span class="name">Rheumatic Heart Disease</span><span class="yn">Yes<span class="o"></span>No<span class="o"></span></span></div>
      <div class="row"><span class="name">Pacemaker</span><span class="yn">Yes<span class="o"></span>No<span class="o"></span></span></div>
      <div class="row"><span class="name">Stent</span><span class="yn">Yes<span class="o"></span>No<span class="o"></span></span></div>
      <div class="gap"></div>
      <div class="group">Other</div>
      <div class="row"><span class="name">Anxiety/PTSD</span><span class="yn">Yes<span class="o"></span>No<span class="o"></span></span></div>
      <div class="row"><span class="name">Arthritis</span><span class="yn">Yes<span class="o"></span>No<span class="o"></span></span></div>
      <div class="row"><span class="name">Alzheimer's</span><span class="yn">Yes<span class="o"></span>No<span class="o"></span></span></div>
      <div class="row"><span class="name">Asthma</span><span class="yn">Yes<span class="o"></span>No<span class="o"></span></span></div>
      <div class="row"><span class="name">Anaphylaxis</span><span class="yn">Yes<span class="o"></span>No<span class="o"></span></span></div>
      <div class="row"><span class="name">Auto-immune disease</span><span class="yn">Yes<span class="o"></span>No<span class="o"></span></span></div>
      <div class="row"><span class="name">Coeliac</span><span class="yn">Yes<span class="o"></span>No<span class="o"></span></span></div>
      <div class="row"><span class="name">Depression</span><span class="yn">Yes<span class="o"></span>No<span class="o"></span></span></div>
      <div class="row"><span class="name">Diabetes</span><span class="yn">Yes<span class="o"></span>No<span class="o"></span></span></div>
      <div class="row"><span class="name">Epilepsy</span><span class="yn">Yes<span class="o"></span>No<span class="o"></span></span></div>
      <div class="row"><span class="name">Kidney Disease</span><span class="yn">Yes<span class="o"></span>No<span class="o"></span></span></div>
      <div class="row"><span class="name">Liver Disease</span><span class="yn">Yes<span class="o"></span>No<span class="o"></span></span></div>
      <div class="row"><span class="name">Osteoporosis</span><span class="yn">Yes<span class="o"></span>No<span class="o"></span></span></div>
      <div class="row"><span class="name">Parkinson's</span><span class="yn">Yes<span class="o"></span>No<span class="o"></span></span></div>
      <div class="row"><span class="name">Radiation to Head/Neck</span><span class="yn">Yes<span class="o"></span>No<span class="o"></span></span></div>
      <div class="row"><span class="name">Schizophrenia</span><span class="yn">Yes<span class="o"></span>No<span class="o"></span></span></div>
      <div class="row"><span class="name">Snoring</span><span class="yn">Yes<span class="o"></span>No<span class="o"></span></span></div>
      <div class="row"><span class="name">Sleep apnea</span><span class="yn">Yes<span class="o"></span>No<span class="o"></span></span></div>
      <div class="row"><span class="name">Stroke</span><span class="yn">Yes<span class="o"></span>No<span class="o"></span></span></div>
    </div>

    <div class="sign" style="left:252px;top:511px;width:240px">Other:<span class="line"></span></div>
    <div class="sign" style="left:7px;top:572px;width:216px">Signature:<span class="line"></span></div>
    <div class="sign" style="left:253px;top:572px;width:240px">Date:<span class="line"></span></div>
  </div>

  <footer class="footer">
    <p class="thanks">Thank you for the time to complete your medical history form.<br>Oral health is linked to overall health and this comprehensive questionnaire will help us to provide you with optimal and safe care.</p>
  </footer>
</section>

</body>
</html>
```